Psychology Practice in Sydney Website Redesign

Corlew Psychology is a Psychology Practice with locations in Westmead, Chatswood and the CBD. They have specialties in treating children, and in treating eating disorders. They also treat anxiety and depression. They have ~10-20 clinical psychologists working for them.

The client wants the site to be modern and professional, he said:
”Mainly gonna be the credibility, people already know of us, but some could find us on google search, site needs to be a bit sexy.”

The client prefers websites with a heavy use of negative space and a largely minimal, modern design. (e.g. https://harbourlanemind-example.com.au/, https://www.fenmora-example.net.au/, https://tovalin-example.com.au/). He wants the site to be approachable without being unprofessional, and to be modern without being clinical. This is their current site: https://www.corlewpsychology-example.com.au/

The client wants the site to be a one pager design (like the sites given above). Please include a section named “Our Specialisations”, and the next titled “What we treat”, then one titled “Our Team” Feel free to take inspiration from the included links for the layout of these parts of the site.

Please mock up a booking panel similar to the that appears when you click "book now" on https://www.quillbrookcare-example.com.au/# .

The client would prefer you use the current logo and colour green (in logo) for theming.

Current site: https://www.corlewpsychology-example.com.au/

The winning designers will be required to:
- Provide a secondary standard page template
- Provide a design for a flyout enquiry/booking form
- Supply all images used in the designs free of charge

```html
<!DOCTYPE html>
<html lang="en">
<head>
<meta charset="utf-8">
<title>Corlew & Associates — Clinical Psychologists</title>
<link rel="stylesheet" href="https://fonts.googleapis.com/css2?family=Montserrat:wght@400;500;600;700&family=Libre+Caslon+Text:wght@400;700&display=swap">
<style>
:root{
  --green:#34a043;
  --green-dark:#2a8a38;
  --green-soft:rgba(108,190,118,.82);
  --grey-soft:rgba(105,105,105,.82);
  --navy:#1d2b3b;
  --ink:#2b2b2b;
  --muted:#555;
  --panel:#eeeeee;
  --footer:#2f2f2f;
  --white:#fff;
  --sans:'Montserrat',sans-serif;
  --serif:'Libre Caslon Text',serif;
}
*{box-sizing:border-box;margin:0;padding:0}
html,body{width:1200px;height:4651px;overflow:hidden}
body{font-family:var(--sans);color:var(--ink);background:var(--white);position:relative}
.abs{position:absolute}
a{color:inherit;text-decoration:none}

.topbar{position:absolute;left:0;top:0;width:1200px;height:36px;background:var(--navy);color:#fff;font-size:11px}
.topbar .follow{position:absolute;left:143px;top:11px;font-weight:600}
.topbar .socials{position:absolute;left:213px;top:0;display:flex}
.topbar .socials span{width:36px;height:36px;display:flex;align-items:center;justify-content:center}
.topbar .socials span:first-child{background:var(--green)}
.topbar .socials i{width:10px;height:10px;border:1.5px solid #fff;display:block}
.topbar .contact{position:absolute;top:11px;display:flex;align-items:center;gap:8px;white-space:nowrap}

.header{position:absolute;top:36px;left:0;width:1200px;height:81px;background:#fff}
.logo{position:absolute;left:143px;top:18px;display:flex;align-items:center;gap:10px}
.logo .mark{width:16px;height:16px;background:var(--green)}
.logo .name{font-weight:700;color:var(--green);font-size:19px;letter-spacing:0;line-height:1;text-transform:uppercase;white-space:nowrap}
.logo .tag{position:absolute;left:26px;top:26px;font-size:8px;letter-spacing:3.2px;color:var(--green);font-weight:700;white-space:nowrap}
.nav{position:absolute;top:33px;font-size:11.5px;font-weight:500;color:#333;white-space:nowrap}
.nav.active{color:var(--green)}
.btn-green{background:var(--green);color:#fff;font-weight:600;font-size:12px;display:flex;align-items:center;justify-content:center;letter-spacing:.4px}

.hero{position:absolute;top:117px;left:0;width:1200px;height:605px;overflow:hidden;
  background:linear-gradient(100deg,#e9efe9 0%,#d5e2cb 30%,#b8cf8f 55%,#9bb85c 75%,#7a9a3a 100%)}
.hero .sky{position:absolute;inset:0;background:radial-gradient(ellipse at 22% 25%,rgba(255,255,255,.8),rgba(255,255,255,0) 55%)}
.hero h1{position:absolute;left:143px;top:100px;font-family:var(--serif);font-weight:400;font-size:54px;line-height:66px;color:#111}
.hero .moved{position:absolute;left:143px;top:243px;font-size:23px;font-weight:500;color:#111}
.hero .cta{position:absolute;left:143px;top:295px;width:130px;height:41px}
.hero svg{position:absolute;left:0;bottom:0}

.about-photo{position:absolute;left:143px;top:758px;width:428px;height:428px;border-radius:50%;background:linear-gradient(135deg,#d9d4cc,#a89584 55%,#6f5e52)}
.about-photo-small{position:absolute;left:417px;top:1021px;width:190px;height:190px;border-radius:50%;border:5px solid #fff;background:linear-gradient(140deg,#e4dfd7,#bba99a 60%,#7c6a5e)}
.eyebrow{position:absolute;left:648px;top:765px;font-size:14px;font-weight:500;display:flex;align-items:center;gap:8px}
.eyebrow::after{content:"";width:38px;height:1px;background:#333}
.about h2{position:absolute;left:648px;top:791px;font-size:31px;font-weight:700;color:var(--green);letter-spacing:.5px;white-space:nowrap}
.about .intro{position:absolute;left:648px;top:837px;width:410px;font-size:12.5px;line-height:22px;color:#333}
.ticks{position:absolute;left:648px;top:890px;width:410px;list-style:none;font-size:12.3px;line-height:19px;color:#444}
.ticks li{position:relative;padding-left:22px;margin-bottom:10px}
.ticks li svg{position:absolute;left:0;top:2px}
.about .book{position:absolute;left:648px;top:1157px;width:130px;height:40px}
.phone-cta{position:absolute;left:803px;top:1155px;display:flex;align-items:center;gap:12px}
.phone-cta .ring{width:42px;height:42px;border-radius:50%;background:#222;display:flex;align-items:center;justify-content:center}
.phone-cta small{display:block;font-size:10px;color:#444}
.phone-cta strong{font-size:15px;font-weight:600}

.label{position:absolute;background:var(--green);color:#fff;font-family:var(--serif);font-size:27px;display:flex;align-items:center;justify-content:center;white-space:nowrap}

.card{position:absolute;top:1399px;width:211px}
.card .img{height:186px;border-radius:14px 14px 0 0}
.card .cap{height:34px;background:#3a3a3a;color:#fff;font-size:13.5px;display:flex;align-items:center;justify-content:center}
.card p{font-size:10px;line-height:20px;text-align:center;padding:6px 10px 0;color:#333}
.card.feature{background:#f2f7f2}
.card .more{position:absolute;top:386px;left:48px;width:113px;height:42px;border:1.5px solid #8cc99a;font-size:12.5px;font-weight:500;display:flex;align-items:center;justify-content:center;background:#fff}

.treat{position:absolute;top:1917px;left:0;width:1200px;height:1007px;overflow:hidden;
  background:linear-gradient(90deg,#c9cfc4 0%,#e8ebe6 40%,#dcd6cc 70%,#b8ad9e 100%)}
.treat .veil{position:absolute;inset:0;background:rgba(255,255,255,.55)}
.treat .lead{position:absolute;left:240px;top:125px;width:720px;text-align:center;font-size:14px;line-height:21px;color:#333}
.treat .sub{position:absolute;left:200px;top:186px;width:800px;text-align:center;font-size:14.5px;font-weight:600}
.treat .lead2{position:absolute;left:230px;top:216px;width:740px;text-align:center;font-size:14px;line-height:21px;color:#333}
.box{position:absolute;width:287px;border-radius:12px;color:#fff;padding:22px 14px 0 14px}
.box.green{background:var(--green-soft)}
.box.grey{background:var(--grey-soft)}
.box h3{font-family:var(--serif);font-weight:400;font-size:20px;margin-bottom:14px}
.box ul{list-style:none;font-size:12.3px;line-height:21px}
.box li{position:relative;padding-left:20px}
.box li::before{content:"";position:absolute;left:2px;top:6px;width:9px;height:9px;border-radius:50%;background:#111}
.box.grey li::before{background:#fff}

.member{position:absolute;top:3087px;width:300px;text-align:center}
.member .photo{width:211px;height:211px;border-radius:50%;margin:0 auto}
.member h4{font-family:var(--serif);font-weight:400;font-size:19px;letter-spacing:1px;margin-top:56px}
.member .cred{font-size:12px;font-weight:600;margin-top:6px}
.member p{font-size:12.3px;line-height:19px;color:#444;margin-top:14px}
.member b{color:#222}
.load{position:absolute;left:531px;top:3597px;width:137px;height:42px;border:1.5px solid #8cc99a;color:var(--green);font-size:12.5px;font-weight:600;display:flex;align-items:center;justify-content:center;gap:8px;background:#fff}

.touch{position:absolute;left:143px;top:3724px;width:915px;height:547px;background:var(--panel);border-radius:38px;z-index:2}
.field{position:absolute;height:38px;background:#fff;border:1px solid #ddd;font-size:12px;color:#444;padding:0 13px;display:flex;align-items:center}
.field .ico{position:absolute;right:0;top:-1px;width:40px;height:38px;background:#5fb870;display:flex;align-items:center;justify-content:center}
.field.area{align-items:flex-start;padding-top:14px}
.submit{position:absolute;left:400px;top:406px;width:127px;height:40px;border:1.5px solid #bbb;background:#fff;font-size:12.5px;font-weight:600;display:flex;align-items:center;justify-content:center}

.footer{position:absolute;left:0;top:4233px;width:1200px;height:368px;background:var(--footer);color:#fff}
.footer .logo{left:143px;top:92px}
.footer .logo .name,.footer .logo .tag{color:#fff}
.footer .logo .mark{background:#fff}
.footer .blurb{position:absolute;left:143px;top:155px;width:270px;font-size:13.5px;line-height:21px}
.footer h5{position:absolute;top:92px;font-size:14px;font-weight:700;letter-spacing:.5px}
.fnav{position:absolute;left:467px;top:138px;list-style:none;font-size:12.5px;line-height:32px}
.fnav li::before{content:"• "}
.fcontact{position:absolute;left:634px;top:138px;font-size:12.5px;line-height:17px}
.fcontact .row{display:flex;gap:14px;margin-bottom:9px}
.fcontact .row i{width:27px;height:27px;border-radius:50%;background:#fff;flex:none;display:flex;align-items:center;justify-content:center}
.fcontact strong{font-size:11.5px}
.fsocial{position:absolute;left:942px;top:136px;font-size:12.5px}
.fsocial div{display:flex;align-items:center;gap:12px;margin-bottom:16px}
.fsocial i{width:28px;height:28px;border-radius:50%;border:1.5px solid #fff}
.copyright{position:absolute;left:0;top:4601px;width:1200px;height:50px;background:#67bd74;font-size:12px;display:flex;align-items:center;justify-content:center;color:#1c1c1c}
</style>
</head>
<body>

<div class="topbar">
  <span class="follow">Follow Us:</span>
  <div class="socials"><span><i></i></span><span><i></i></span><span><i></i></span><span><i></i></span></div>
  <span class="contact" style="left:720px">
    <svg width="13" height="13" viewBox="0 0 24 24"><path fill="#4cb35c" d="M6.6 10.8a15 15 0 0 0 6.6 6.6l2.2-2.2c.3-.3.7-.4 1-.2 1.1.4 2.3.6 3.6.6.6 0 1 .4 1 1V20c0 .6-.4 1-1 1A17 17 0 0 1 3 4c0-.6.4-1 1-1h3.5c.6 0 1 .4 1 1 0 1.3.2 2.5.6 3.6.1.3 0 .7-.2 1z"/></svg>(02) 9000 1766</span>
  <span class="contact" style="left:840px">
    <svg width="14" height="11" viewBox="0 0 24 18"><rect x="1" y="1" width="22" height="16" fill="#4cb35c"/><path d="M1 1l11 9 11-9" stroke="#1d2b3b" stroke-width="2" fill="none"/></svg>info@corlewpsychology-example.com.au</span>
</div>

<header class="header">
  <div class="logo"><span class="mark"></span><span class="name">Corlew &amp; Associates</span><span class="tag">CLINICAL PSYCHOLOGISTS</span></div>
  <a class="nav active" style="left:457px">HOME</a>
  <a class="nav" style="left:520px">ABOUT</a>
  <a class="nav" style="left:590px">SPECIALIST CLINICS</a>
  <a class="nav" style="left:755px">RESOURCES</a>
  <a class="nav" style="left:859px">CONTACT</a>
  <a class="btn-green abs" style="left:942px;top:18px;width:116px;height:42px">BOOK NOW</a>
</header>

<section class="hero" role="img" aria-label="Woman with arms open in a sunlit grassy meadow with hills behind">
  <div class="sky"></div>
  <h1>Chatswood<br>Has Moved!</h1>
  <p class="moved">We are now in 4, 18 Elm St.</p>
  <a class="btn-green cta">BOOK NOW</a>
  <svg width="1200" height="230" viewBox="0 0 1200 230">
    <path d="M0 95 C200 20 420 200 760 205 C950 208 1100 165 1200 125 L1200 230 L0 230Z" fill="#2f9a3f"/>
    <path d="M0 125 C220 55 430 215 760 218 C950 220 1100 180 1200 152 L1200 230 L0 230Z" fill="#fff"/>
  </svg>
</section>

<section class="about">
  <div class="about-photo" role="img" aria-label="Doctor examining a young child held by a parent"></div>
  <div class="about-photo-small" role="img" aria-label="Psychologist in a consultation with a client"></div>
  <div class="eyebrow">Who We Are</div>
  <h2>CORLEW &amp; ASSOCIATES</h2>
  <p class="intro">We differ from other practices in several ways. At Corlew and Associates:</p>
  <ul class="ticks">
    <li><svg width="14" height="14" viewBox="0 0 16 16"><circle cx="8" cy="8" r="8" fill="#34a043"/><path d="M4.5 8.2l2.3 2.3 4.7-4.8" stroke="#fff" stroke-width="1.8" fill="none"/></svg>We are all clinical psychologists with post-graduate clinical training.</li>
    <li><svg width="14" height="14" viewBox="0 0 16 16"><circle cx="8" cy="8" r="8" fill="#34a043"/><path d="M4.5 8.2l2.3 2.3 4.7-4.8" stroke="#fff" stroke-width="1.8" fill="none"/></svg>We have enough specialists in different conditions, so you will find the right psychologist to work with you.</li>
    <li><svg width="14" height="14" viewBox="0 0 16 16"><circle cx="8" cy="8" r="8" fill="#34a043"/><path d="M4.5 8.2l2.3 2.3 4.7-4.8" stroke="#fff" stroke-width="1.8" fill="none"/></svg>Our clinicians are committed to staying up to date with research into the causes and treatments of common conditions.</li>
    <li><svg width="14" height="14" viewBox="0 0 16 16"><circle cx="8" cy="8" r="8" fill="#34a043"/><path d="M4.5 8.2l2.3 2.3 4.7-4.8" stroke="#fff" stroke-width="1.8" fill="none"/></svg>We only use treatments that have a known basis of evidence showing them to be effective. We then adapt and tailor these treatments to each individual after a thorough assessment.</li>
  </ul>
  <a class="btn-green book">BOOK NOW</a>
  <div class="phone-cta">
    <span class="ring"><svg width="20" height="20" viewBox="0 0 24 24"><path fill="#fff" d="M6.6 10.8a15 15 0 0 0 6.6 6.6l2.2-2.2c.3-.3.7-.4 1-.2 1.1.4 2.3.6 3.6.6.6 0 1 .4 1 1V20c0 .6-.4 1-1 1A17 17 0 0 1 3 4c0-.6.4-1 1-1h3.5c.6 0 1 .4 1 1 0 1.3.2 2.5.6 3.6.1.3 0 .7-.2 1z"/></svg></span>
    <span><small>Contact Us Today</small><strong>(02) 9000 1766</strong></span>
  </div>
</section>

<section class="specialisations">
  <h2 class="label" style="left:455px;top:1325px;width:292px;height:44px">Our Specialisations</h2>
  <article class="card" style="left:143px">
    <div class="img" role="img" aria-label="Clinician assessing a distressed young person" style="background:linear-gradient(135deg,#e5e3df,#b9b2a8 60%,#7d7469)"></div>
    <div class="cap">Psychometric Assessments</div>
    <p>We offer detailed tests and reports on children and teens, including for school or learning problems and ADHD. For further information refer to our Child and Family arm of the practice or call <b>02 9000 4099</b>.</p>
    <a class="more">View Details</a>
  </article>
  <article class="card feature" style="left:377px">
    <div class="img" role="img" aria-label="Person wearing a virtual reality headset beside a clinician" style="background:linear-gradient(135deg,#4b6f8f,#2d4a66 55%,#1c2f44)"></div>
    <div class="cap">Virtual Reality Clinic</div>
    <p>We have the combined software and hardware to provide VR-based treatments of phobias, especially for fears of flying, driving in tunnels, heights, closed spaces, public speaking, dogs and several other situations...</p>
    <a class="more">View Details</a>
  </article>
  <article class="card" style="left:612px">
    <div class="img" role="img" aria-label="Child looking unhappily at a plate of pasta" style="background:linear-gradient(135deg,#d8c6ae,#b38d68 55%,#6e5440)"></div>
    <div class="cap">Eating Disorders</div>
    <p>We provide assessment and treatment of all eating disorders, including anorexia nervosa, bulimia nervosa, binge eating, picky and avoidant eating (ARFID), and nocturnal eating syndrome. Our clinicians undergo...</p>
    <a class="more">View Details</a>
  </article>
  <article class="card" style="left:847px">
    <div class="img" role="img" aria-label="Woman holding her head in discomfort" style="background:linear-gradient(135deg,#e8ddd2,#c7ab92 55%,#8c6f58)"></div>
    <div class="cap">FND and Somatisation</div>
    <p>Functional Neurological Disorder (FND) is another term for conversion disorder, which is when a person's central nervous system is generating symptoms even though the body is fine and healthy...</p>
    <a class="more">View Details</a>
  </article>
</section>

<section class="treat" role="img" aria-label="Soft background of a mother smiling with her child">
  <div class="veil"></div>
  <h2 class="label" style="left:491px;top:63px;width:226px;height:40px">What we treat</h2>
  <p class="lead">You may be surprised to learn how common psychological problems are, and how commonly our emotions stop us from achieving the happiness that we could otherwise attain.</p>
  <h3 class="sub">Issues We Can Help You With</h3>
  <p class="lead2">Clinical Psychologists have the skills to help people with a wide range of problems. Look below for a list of issues that our clinical psychologists have the knowledge and techniques to help people with:</p>

  <div class="box green" style="left:143px;top:298px;height:337px"><h3>Mood</h3><ul><li>Depression</li><li>Bipolar disorder ('manic depression')</li><li>Low self-esteem</li><li>Grief</li><li>Post-natal depression</li></ul></div>
  <div class="box grey" style="left:457px;top:298px;height:337px"><h3>Anxiety</h3><ul><li>Phobias</li><li>Worry</li><li>Shyness, social anxiety and public speaking</li><li>Panic</li><li>Obsessive thoughts and compulsions (OCD)</li><li>Needle phobia / Medical procedures</li><li>Managing stress better (exams, work etc...)</li><li>For an outline of all anxiety disorders</li></ul></div>
  <div class="box green" style="left:771px;top:298px;height:337px"><h3>Eating Disorders</h3><ul><li>Bulimia nervosa and other binge-eating disorders</li><li>Restrictive and low weight eating disorders (anorexia nervosa)</li><li>Trouble accepting your body</li><li>To understand why eating disorders are serious problems</li></ul></div>
  <div class="box grey" style="left:143px;top:655px;height:265px"><h3>Trauma</h3><ul><li>Emotional recovery after a motor vehicle accident</li><li>Other accidents or assaults leading to Post-traumatic stress</li><li>Sexual / physical / emotional abuse</li></ul></div>
  <div class="box green" style="left:457px;top:655px;height:265px"><h3>Physical Health</h3><ul><li>Adjusting to a serious injury or illness</li><li>Managing Chronic Pain</li><li>Tinnitus</li><li>Sleeping Difficulties</li><li>Quit smoking</li><li>Manage your alcohol consumption</li></ul></div>
  <div class="box grey" style="left:771px;top:655px;height:265px"><h3>Skills to Enhance Your Life</h3><ul><li>Self-esteem</li><li>Assertiveness and other Communication skills</li><li>Increase motivation</li><li>Interpersonal difficulties</li><li>Learn relaxation or buy our CDs</li><li>Learn meditation and how it can enhance your life</li></ul></div>
</section>

<section class="team">
  <h2 class="label" style="left:518px;top:3009px;width:164px;height:40px">Our Team</h2>
  <div class="member" style="left:137px">
    <div class="photo" role="img" aria-label="Portrait of Clara Whitfield" style="background:linear-gradient(135deg,#e6d3b8,#b89268 55%,#6d5238)"></div>
    <h4>CLARA WHITFIELD</h4>
    <div class="cred">B.Psych (Hons), M.Psych (Clinical)</div>
    <p>Clara is a Clinical Psychology Registrar who completed her Master of Clinical Psychology and Bachelor of Psychology (Honours) at Harbourview University. Clara has worked with children, adolescents, and adults with a range of presentations, including anxiety...<b>[+]</b></p>
  </div>
  <div class="member" style="left:451px">
    <div class="photo" role="img" aria-label="Portrait of Daniel Okoye" style="background:linear-gradient(135deg,#c9c4bb,#8a7a6a 55%,#3e342c)"></div>
    <h4>DANIEL OKOYE</h4>
    <div class="cred">B.Psych.(Hons); M.Psychol.</div>
    <p>Daniel completed his Master of Clinical Psychology at Eastbridge University, and has worked in various settings including inpatient and outpatient care at a private psychiatric hospital and across several clinical research units. From those collaborations, his professional publications...<b>[+]</b></p>
  </div>
  <div class="member" style="left:767px">
    <div class="photo" role="img" aria-label="Portrait of Mira Lindqvist" style="background:linear-gradient(135deg,#e9dccb,#bf9a78 55%,#6e4e36)"></div>
    <h4>MIRA LINDQVIST</h4>
    <div class="cred">B.Sc. (Psych)(Hons); MClinPsych</div>
    <p>Mira is a Clinical Psychology Registrar who completed her Master of Clinical Psychology at Eastbridge University after gaining a Bachelor of Science with Psychology Honours at Westgate University. Mira has experience working with individuals and...<b>[+]</b></p>
  </div>
  <a class="load">Load More <svg width="18" height="18" viewBox="0 0 20 20"><circle cx="10" cy="10" r="8.5" fill="none" stroke="#34a043" stroke-width="1.4"/><path d="M6.5 8.5l3.5 3.5 3.5-3.5" fill="none" stroke="#34a043" stroke-width="1.4"/></svg></a>
</section>

<section class="touch">
  <h2 class="label" style="left:356px;top:103px;width:203px;height:40px">Get in Touch</h2>
  <div class="field" style="left:59px;top:187px;width:247px">Full Name *
    <span class="ico"><svg width="18" height="18" viewBox="0 0 24 24" fill="none" stroke="#fff" stroke-width="1.6"><circle cx="12" cy="8" r="4"/><path d="M4 21c0-4.4 3.6-7 8-7s8 2.6 8 7z"/></svg></span></div>
  <div class="field" style="left:332px;top:187px;width:245px">Email Address *
    <span class="ico"><svg width="18" height="14" viewBox="0 0 24 18" fill="none" stroke="#fff" stroke-width="1.6"><rect x="1" y="1" width="22" height="16"/><path d="M1 1l11 9 11-9"/></svg></span></div>
  <div class="field" style="left:604px;top:187px;width:246px">Subject
    <span class="ico"><svg width="18" height="18" viewBox="0 0 24 24"><path fill="none" stroke="#fff" stroke-width="1.6" d="M6.6 10.8a15 15 0 0 0 6.6 6.6l2.2-2.2c.3-.3.7-.4 1-.2 1.1.4 2.3.6 3.6.6.6 0 1 .4 1 1V20c0 .6-.4 1-1 1A17 17 0 0 1 3 4c0-.6.4-1 1-1h3.5c.6 0 1 .4 1 1 0 1.3.2 2.5.6 3.6.1.3 0 .7-.2 1z"/></svg></span></div>
  <div class="field area" style="left:59px;top:243px;width:791px;height:140px">Your Message *
    <span class="ico"><svg width="20" height="18" viewBox="0 0 24 22" fill="none" stroke="#fff" stroke-width="1.6"><path d="M2 2h14v10H8l-4 3v-3H2z"/><path d="M18 7h4v10h-2v3l-4-3h-6v-3"/></svg></span></div>
  <a class="submit">SUBMIT NOW</a>
</section>

<footer class="footer">
  <div class="logo"><span class="mark"></span><span class="name">Corlew &amp; Associates</span><span class="tag">CLINICAL PSYCHOLOGISTS</span></div>
  <p class="blurb">Lorem ipsum dolor sit amet, consecte tuer adipiscing elit, sesesfd diam inn nonummy nibh euismod tincidunt ut laoreet dolore magna aliquam erat volutpat.</p>
  <h5 style="left:467px">NAVIGATION</h5>
  <ul class="fnav"><li>Home</li><li>About</li><li>Specialist Clinic</li><li>Resources</li><li>Contact</li></ul>
  <h5 style="left:634px">CONTACT US</h5>
  <div class="fcontact">
    <div class="row"><i><svg width="12" height="14" viewBox="0 0 12 16"><path d="M6 0a6 6 0 0 0-6 6c0 4.5 6 10 6 10s6-5.5 6-10a6 6 0 0 0-6-6z" fill="#2f2f2f"/><circle cx="6" cy="6" r="2" fill="#fff"/></svg></i><span>Corlew &amp; Associates<br>PO Box 512, Larkfield NSW 2199</span></div>
    <div class="row"><i><svg width="13" height="13" viewBox="0 0 24 24"><path fill="#2f2f2f" d="M6.6 10.8a15 15 0 0 0 6.6 6.6l2.2-2.2c.3-.3.7-.4 1-.2 1.1.4 2.3.6 3.6.6.6 0 1 .4 1 1V20c0 .6-.4 1-1 1A17 17 0 0 1 3 4c0-.6.4-1 1-1h3.5c.6 0 1 .4 1 1 0 1.3.2 2.5.6 3.6.1.3 0 .7-.2 1z"/></svg></i><span><strong>PHONE</strong><br>(02) 9000 1766</span></div>
    <div class="row"><i><svg width="14" height="13" viewBox="0 0 24 22" fill="none" stroke="#2f2f2f" stroke-width="2"><rect x="3" y="8" width="18" height="11"/><path d="M7 8V2h10v6M7 13h10"/></svg></i><span><strong>FAX</strong><br>(02) 9000 6122</span></div>
    <div class="row"><i><svg width="13" height="10" viewBox="0 0 24 18" fill="none" stroke="#2f2f2f" stroke-width="2.2"><rect x="1" y="1" width="22" height="16"/><path d="M1 1l11 9 11-9"/></svg></i><span><strong>EMAIL</strong><br>info@corlewpsychology-example.com.au</span></div>
  </div>
  <h5 style="left:942px">FOLLOW US</h5>
  <div class="fsocial">
    <div><i></i>Friendline</div>
    <div><i></i>Chirpwave</div>
    <div><i></i>Snapgallery</div>
    <div><i></i>Careerlink</div>
  </div>
</footer>
<div class="copyright">Copyright © 2024 Corlew Psychology. All Rights Reserved.</div>

</body>
</html>
```